Providing Back Office Solutions to Financial Advisors and Attorney Needs a Business Card Design

Need a Business Card Design that speaks to Financial Advisor and Attorneys. Some of the word that come to mind is Clean/Simple & Futuristic.

Industry/Entity Type

Business

```html
<!DOCTYPE html>
<html lang="en">
<head>
<meta charset="utf-8">
<title>Kairon Back Office Solutions – Business Card</title>
<link rel="stylesheet" href="https://fonts.googleapis.com/css2?family=Roboto+Condensed:wght@500&family=Open+Sans:wght@400;600&display=swap">
<style>
  :root {
    --backdrop: #bcbcbc;
    --blue-deep: #0b4473;
    --blue-bright: #0b69a5;
    --navy-text: #133d72;
    --white: #ffffff;
    --paper: #f1f1f1;
    --violet-edge: #4a3f9a;
    --rule: #1b4f86;
  }
  * { box-sizing: border-box; margin: 0; padding: 0; }
  html, body { width: 1200px; height: 576px; overflow: hidden; }
  body {
    position: relative;
    background: var(--backdrop);
    font-family: "Open Sans", Arial, sans-serif;
  }
  .card {
    position: absolute;
    top: 138px;
    width: 484px;
    height: 292px;
    border-radius: 12px;
    overflow: hidden;
  }
  .card-front {
    left: 82px;
    background: linear-gradient(180deg, var(--blue-deep) 0%, var(--blue-bright) 50%, var(--blue-deep) 100%);
  }
  .card-back { left: 602px; width: 480px; height: 290px; background: var(--paper); }

  .brand-name {
    font-family: "Roboto Condensed", Arial, sans-serif;
    font-weight: 500;
    text-align: center;
    line-height: 1;
  }
  .card-front .brand-name {
    position: absolute;
    left: 0; right: 0; top: 108px;
    color: var(--white);
  }
  .brand-word { display: block; font-size: 54px; letter-spacing: 3px; }
  .brand-tagline { display: block; font-size: 19px; margin-top: 10px; letter-spacing: 0.3px; }

  .card-back .brand-block {
    position: absolute;
    left: 28px; width: 170px; top: 90px;
  }
  .card-back .brand-rule { height: 1.5px; background: var(--rule); margin-bottom: 10px; }
  .card-back .brand-name { color: var(--navy-text); }
  .card-back .brand-word { font-size: 40px; letter-spacing: 2px; }
  .card-back .brand-tagline { font-size: 14px; margin-top: 8px; }

  .contact-panel { position: absolute; inset: 0; }

  .contact-details {
    position: absolute;
    left: 276px; top: 60px;
    color: var(--white);
  }
  .person-name { font-size: 18px; font-weight: 600; letter-spacing: 0.2px; }
  .person-role { font-size: 12px; margin-top: 4px; }
  .address { font-size: 12px; line-height: 18px; margin-top: 36px; }
  .contact-list { list-style: none; margin-top: 12px; }
  .contact-list li {
    display: flex; align-items: center;
    font-size: 12px; height: 17px;
  }
  .contact-list svg { width: 10px; height: 10px; margin-right: 13px; flex: none; }
</style>
</head>
<body>

  <section class="card card-front" aria-label="Card front">
    <h1 class="brand-name">
      <span class="brand-word">KAIRON</span>
      <span class="brand-tagline">BACK OFFICE SOLUTIONS</span>
    </h1>
  </section>

  <section class="card card-back" aria-label="Card back">
    <div class="brand-block">
      <div class="brand-rule"></div>
      <h2 class="brand-name">
        <span class="brand-word">KAIRON</span>
        <span class="brand-tagline">BACK OFFICE SOLUTIONS</span>
      </h2>
    </div>

    <svg class="contact-panel" width="480" height="290" viewBox="0 0 480 290" aria-hidden="true">
      <defs>
        <linearGradient id="panelBlue" x1="0" y1="0" x2="0" y2="1">
          <stop offset="0" stop-color="#0b4473"/>
          <stop offset="0.5" stop-color="#0b69a5"/>
          <stop offset="1" stop-color="#0b4473"/>
        </linearGradient>
      </defs>
      <path d="M252 0 L216 62 Q212 70 212 80 L212 214 Q212 224 216 232 L246 290 L480 290 L480 0 Z" fill="#4a3f9a"/>
      <path d="M258 0 L222 62 Q218 70 218 80 L218 214 Q218 224 222 232 L252 290 L480 290 L480 0 Z" fill="url(#panelBlue)"/>
    </svg>

    <div class="contact-details">
      <p class="person-name">John Doe Smith</p>
      <p class="person-role">Managing Director</p>
      <p class="address">234 Anywhere St.,<br>Any Town, US 123456</p>
      <ul class="contact-list">
        <li>
          <svg viewBox="0 0 10 10" aria-hidden="true"><path d="M0.5 3.5 Q5 0.5 9.5 3.5 L8.5 4.8 L7 4 L7 3.2 Q5 2.6 3 3.2 L3 4 L1.5 4.8 Z M2 5.5 L8 5.5 L9 9.2 L1 9.2 Z" fill="#fff"/></svg>
          555.555.5555
        </li>
        <li>
          <svg viewBox="0 0 10 10" aria-hidden="true"><rect x="0.5" y="2" width="9" height="6.4" fill="#fff"/><path d="M0.8 2.3 L5 5.6 L9.2 2.3" stroke="#0b5a92" stroke-width="0.9" fill="none"/></svg>
          johndoe@example.com
        </li>
        <li>
          <svg viewBox="0 0 10 10" aria-hidden="true"><g fill="none" stroke="#fff" stroke-width="0.9"><circle cx="5" cy="5" r="4.3"/><ellipse cx="5" cy="5" rx="1.8" ry="4.3"/><path d="M0.7 5 H9.3 M1.5 2.8 H8.5 M1.5 7.2 H8.5"/></g></svg>
          www.yourwebsite.com
        </li>
      </ul>
    </div>
  </section>

</body>
</html>
```